Website for a Construction Business That Builds Houses

We want some design concepts for this website. Customer likes this competitor site: https://brenwickdwellings.com.au/

We have a logo for Tarvond Constructions. Logo font is Birdman, attached with AI.

Want to be able to change hero images

Will have a contact page.

Need to know what plugins will be used for WordPress.

Coding

Coded - Design and coding required

```html
<!DOCTYPE html>
<html lang="en">
<head>
<meta charset="utf-8">
<title>Tarvond Constructions</title>
<link href="https://fonts.googleapis.com/css2?family=Jost:wght@400;500&family=Playfair+Display:wght@600;700&display=swap" rel="stylesheet">
<style>
:root{
  --green:#8dc63f;
  --dark:#3a3d47;
  --ink:#1f2024;
  --muted:#8b8d93;
  --light:#f5f5f5;
  --field:#f3f3f3;
  --white:#ffffff;
  --serif:"Playfair Display", Georgia, serif;
  --sans:"Jost", Arial, sans-serif;
}
*{box-sizing:border-box;margin:0;padding:0}
html,body{width:1200px;height:5020px;overflow:hidden;background:var(--white);font-family:var(--sans);color:var(--ink)}
.page{position:relative;width:1200px;height:5020px}
section,header,footer,nav{position:absolute;left:0;width:1200px}
.btn{position:absolute;display:flex;align-items:center;justify-content:center;font-family:var(--sans);font-size:15px;letter-spacing:.5px;text-transform:uppercase}
.btn-solid{background:var(--green);color:var(--white)}
.btn-outline-white{border:3px solid var(--white);color:var(--white)}
.btn-outline-green{border:3px solid var(--green);color:var(--green);background:var(--white)}
.photo{position:absolute}

/* top bar */
.topbar{top:0;height:45px;background:var(--dark);color:var(--white)}
.topbar .social{position:absolute;left:46px;top:13px;display:flex;gap:22px}
.topbar .dot{width:18px;height:18px;border-radius:50%;background:var(--white)}
.topbar .info{position:absolute;top:14px;font-size:11px;display:flex;align-items:center;gap:7px}
.topbar .cta{position:absolute;left:939px;top:0;width:189px;height:45px;background:var(--green);display:flex;align-items:center;justify-content:center;font-size:18px;text-transform:uppercase}

/* nav */
.nav{top:45px;height:107px;background:var(--white)}
.brand{position:absolute;left:40px;top:30px;display:flex;align-items:center;gap:10px;font-size:16px;line-height:19px;font-weight:500;color:var(--ink)}
.brand .mark{width:24px;height:24px;border-radius:50%;background:var(--green);flex:none}
.nav ul{list-style:none;position:absolute;top:52px;left:238px;font-size:15px;text-transform:uppercase}
.nav li{position:absolute;white-space:nowrap}

/* hero */
.hero{top:152px;height:582px}
.hero-panel{position:absolute;left:0;top:0;width:610px;height:582px;background:var(--green)}
.hero h1{position:absolute;left:80px;top:204px;white-space:nowrap;font-family:var(--serif);font-weight:600;font-size:40px;color:var(--white);line-height:1}
.hero p{position:absolute;left:80px;top:275px;width:470px;font-size:17px;line-height:28px;color:var(--white)}

/* about */
.about{top:734px;height:698px}
.years{position:absolute;left:647px;top:152px}
.years .frame{position:absolute;left:0;top:0;width:97px;height:146px;border:6px solid #d9d9db;border-right:none}
.years .num{position:absolute;left:50px;top:28px;font-family:var(--sans);font-size:78px;font-weight:500;color:var(--green);line-height:1}
.years .label{position:absolute;left:160px;top:58px;white-space:nowrap;font-family:var(--serif);font-size:20px;font-weight:600}
.about h2{position:absolute;left:651px;top:323px;font-family:var(--serif);font-size:28px;font-weight:600}
.about p{position:absolute;left:652px;top:374px;width:484px;font-size:13px;line-height:22px;color:var(--muted)}

/* rebuild */
.rebuild{top:1432px;height:450px;background:var(--light)}
.eyebrow{font-size:17px;color:var(--green);text-transform:uppercase}
.rebuild .eyebrow{position:absolute;left:124px;top:104px;text-transform:none}
.rebuild h2{position:absolute;left:120px;top:140px;font-family:var(--serif);font-size:33px;line-height:42px;font-weight:600}

/* packages */
.packages{top:1882px;height:734px}
.packages h2{position:absolute;left:0;width:1200px;top:138px;text-align:center;font-family:var(--serif);font-size:32px;font-weight:600}
.package{position:absolute;top:272px;width:300px;text-align:center}
.package svg{display:block;margin:0 auto}
.package h3{margin-top:40px;font-family:var(--serif);font-size:24px;line-height:30px;font-weight:600}
.package p{margin:12px auto 0;width:262px;font-size:10.5px;line-height:14px;color:var(--muted)}

/* feature rows */
.feature{height:437px}
.feature-box{position:absolute;width:485px;height:337px;padding:72px 0 0 88px}
.feature-box.green{background:var(--green);color:var(--white)}
.feature-box.white{background:var(--white);color:var(--ink)}
.feature-box .eyebrow{font-size:14px;color:inherit}
.feature-box.white .eyebrow{color:var(--green)}
.feature-box h3{margin-top:12px;font-family:var(--serif);font-size:29px;line-height:37px;font-weight:600}

/* contact */
.contact{top:3921px;height:715px}
.contact h2{position:absolute;left:0;width:1165px;top:124px;text-align:center;font-family:var(--serif);font-size:40px;font-weight:600}
.field{position:absolute;background:var(--field);font-size:14px;color:#55575c;padding:14px 0 0 18px}
.submit{position:absolute;left:230px;top:483px;width:699px;height:69px;background:var(--green);color:var(--white);font-size:28px;display:flex;align-items:center;justify-content:center;text-transform:uppercase}

/* footer */
.footer{top:4636px;height:384px;background:var(--dark);color:var(--white)}
.footer-brand{position:absolute;left:64px;top:109px;width:156px;height:156px;border-radius:50%;background:var(--white);display:flex;align-items:center;justify-content:center;text-align:center;font-size:20px;font-weight:500;color:var(--ink);line-height:24px}
.footer h4{position:absolute;top:100px;font-family:var(--serif);font-size:20px;font-weight:600}
.footer .line{position:absolute;font-size:13px;display:flex;align-items:center;gap:12px;color:#e6e7ea}
.footer .link{position:absolute;font-size:13px;color:#e6e7ea}
.footer .social{position:absolute;left:938px;top:197px;display:flex;gap:34px}
.footer .social span{width:20px;height:20px;border-radius:50%;background:var(--green)}
</style>
</head>
<body>
<div class="page">

<header class="topbar">
  <div class="social"><span class="dot"></span><span class="dot"></span><span class="dot"></span></div>
  <div class="info" style="left:596px">
    <svg width="12" height="12" viewBox="0 0 24 24"><path fill="#fff" d="M6.6 10.8a15 15 0 0 0 6.6 6.6l2.2-2.2c.3-.3.7-.4 1-.2 1.1.4 2.3.6 3.6.6.6 0 1 .4 1 1V20c0 .6-.4 1-1 1A17 17 0 0 1 3 4c0-.6.4-1 1-1h3.5c.6 0 1 .4 1 1 0 1.3.2 2.5.6 3.6.1.3 0 .7-.2 1z"/></svg>
    +61 2 5550 0142
  </div>
  <div class="info" style="left:752px">
    <svg width="14" height="11" viewBox="0 0 24 18"><rect x="1" y="1" width="22" height="16" rx="2" fill="#fff"/><path d="M2 2l10 8 10-8" stroke="#3a3d47" stroke-width="2" fill="none"/></svg>
    support@domain.com
  </div>
  <div class="cta">Contact us</div>
</header>

<nav class="nav">
  <div class="brand"><span class="mark"></span><span>Tarvond<br>Constructions</span></div>
  <ul>
    <li style="left:0">Home</li>
    <li style="left:111px">About</li>
    <li style="left:224px">Home Designs</li>
    <li style="left:412px">Display Homes</li>
    <li style="left:602px">Custom Build</li>
    <li style="left:770px">House Rebuild</li>
  </ul>
</nav>

<section class="hero">
  <div class="hero-panel"></div>
  <h1>Tarvond Constructions</h1>
  <p>Building your own home is an experience of a lifetime. Who you choose to work with on your journey can make the world of difference.</p>
  <div class="btn btn-outline-white" style="left:81px;top:380px;width:169px;height:44px">Contact us</div>
  <div class="photo" role="img" aria-label="Living room with wood-panelled ceiling, fireplace and sheepskin chair" style="left:610px;top:0;width:590px;height:582px;background:linear-gradient(135deg,#6b5443 0%,#4a3a30 45%,#8a7a68 75%,#3c4a3a 100%)"></div>
</section>

<section class="about">
  <div class="photo" role="img" aria-label="White modern villa beside a pool under misty hills" style="left:66px;top:106px;width:431px;height:401px;background:linear-gradient(180deg,#6f8a8c 0%,#c9d1d0 40%,#efefec 60%,#7a5f4c 100%)"></div>
  <div class="photo" role="img" aria-label="Lavender living room with sofa and framed pictures" style="left:296px;top:322px;width:285px;height:267px;background:linear-gradient(180deg,#b3b6dc 0%,#9c9fca 55%,#6a79a8 75%,#c8c6c2 100%)"></div>
  <div class="years">
    <div class="frame"></div>
    <div class="num">25</div>
    <div class="label">Years of Experience</div>
  </div>
  <h2>Embrace the joy of your new home.</h2>
  <p>Building your own home is an experience of a lifetime. Who you choose to work with on your journey can make the world of difference. At Brenwick Dwellings Homes our focus is you, the client. We work hard to ensure you're delighted—not just with the end result—but with the entire building process.</p>
  <div class="btn btn-solid" style="left:656px;top:489px;width:150px;height:33px;font-size:14px">Read more</div>
</section>

<section class="rebuild">
  <div class="eyebrow">Knock Down Rebuild</div>
  <h2>Check out our<br>latest knockdown<br>rebuild project here.</h2>
  <div class="btn btn-solid" style="left:121px;top:290px;width:171px;height:41px">Read more</div>
  <div class="btn btn-outline-green" style="left:305px;top:290px;width:176px;height:41px">Watch video</div>
  <div class="photo" role="img" aria-label="Open-plan living area with timber ceiling, plaid sofa and pool view" style="left:614px;top:0;width:586px;height:450px;background:linear-gradient(160deg,#7a4a2c 0%,#a46b43 35%,#d9cfc4 65%,#8a7866 100%)"></div>
</section>

<section class="packages">
  <h2>A package that fits any budget.</h2>
  <div class="package" style="left:113px">
    <svg width="118" height="118" viewBox="0 0 118 118" fill="none" stroke="#8dc63f" stroke-width="3">
      <rect x="18" y="12" width="82" height="20"/><rect x="18" y="32" width="82" height="64"/>
      <rect x="28" y="42" width="46" height="18"/><path d="M38 42v18M48 42v18M58 42v18M66 42v18"/>
      <rect x="62" y="68" width="30" height="28"/><path d="M10 96h98M66 76h22M66 84h22"/>
    </svg>
    <h3>A new level of<br>inspired living.</h3>
    <p>The Inspire range offer great affordability coupled with stylish finishes that are perfectly suited for the growing family, first timers or savvy investors.</p>
  </div>
  <div class="package" style="left:464px">
    <svg width="126" height="118" viewBox="0 0 126 118" fill="none" stroke="#8dc63f" stroke-width="3">
      <path d="M10 62 58 20l48 42M22 52v46h74V52"/><circle cx="104" cy="18" r="8"/>
      <path d="M104 2v5M104 29v5M88 18h5M115 18h5M93 7l3 3M112 26l3 3M115 7l-3 3"/>
      <path d="M40 92V76c0-4 4-7 8-7h22c4 0 8 3 8 7v16M36 80h46M52 44h12v10H52z"/>
    </svg>
    <h3>Live a life that<br>stands out.</h3>
    <p>The Inspire range offer great affordability coupled with stylish finishes that are perfectly suited for the growing family, first timers or savvy investors.</p>
  </div>
  <div class="package" style="left:822px">
    <svg width="122" height="130" viewBox="0 0 122 130" fill="none" stroke="#8dc63f" stroke-width="3">
      <path d="M36 46h50l14 14-39 40-39-40z"/><path d="M22 60h78M50 46l-6 14 17 40 17-40-6-14"/>
      <path d="M61 4v16M32 14l8 12M90 14l-8 12M8 40l14 6M114 40l-14 6M61 108v12M38 104l-6 10M84 104l6 10"/>
    </svg>
    <h3>An inspired level<br>of living</h3>
    <p>The Inspire range offer great affordability coupled with stylish finishes that are perfectly suited for the growing family, first timers or savvy investors.</p>
  </div>
  <div class="btn btn-solid" style="left:175px;top:582px;width:176px;height:39px">Read more</div>
  <div class="btn btn-solid" style="left:527px;top:582px;width:176px;height:39px">Read more</div>
  <div class="btn btn-solid" style="left:887px;top:582px;width:176px;height:39px">Read more</div>
</section>

<section class="feature" style="top:2616px">
  <div class="photo" role="img" aria-label="Two-storey modern house with timber cladding and garage" style="left:0;top:0;width:1200px;height:437px;background:linear-gradient(180deg,#dfe2e4 0%,#b9bdbd 40%,#5c5a57 70%,#6f7b57 100%)"></div>
  <div class="feature-box green" style="left:660px;top:53px">
    <div class="eyebrow">Custom Design</div>
    <h3>Beautifully crafted<br>luxury homes you'll<br>fall in love with.</h3>
  </div>
  <div class="btn btn-outline-white" style="left:746px;top:286px;width:158px;height:39px;font-size:14px">Read more</div>
</section>

<section class="feature" style="top:3053px">
  <div class="photo" role="img" aria-label="Timber-walled lounge with fireplace, television and hanging chair" style="left:0;top:0;width:1200px;height:434px;background:linear-gradient(135deg,#5d4a3c 0%,#3b3430 40%,#7d6c5a 70%,#44523e 100%)"></div>
  <div class="feature-box white" style="left:76px;top:58px">
    <div class="eyebrow">Design Studio</div>
    <h3>Luxury hand crafted<br>homes that you will<br>fall in love with</h3>
  </div>
  <div class="btn btn-solid" style="left:185px;top:312px;width:155px;height:33px;font-size:14px">Read more</div>
</section>

<section class="feature" style="top:3487px">
  <div class="photo" role="img" aria-label="Bright room with black steel-framed glass doors and coffee table" style="left:0;top:0;width:1200px;height:434px;background:linear-gradient(135deg,#8a7e70 0%,#d9d6d0 35%,#b8ab98 65%,#6a5e52 100%)"></div>
  <div class="feature-box green" style="left:658px;top:53px">
    <div class="eyebrow">Custom Design</div>
    <h3>Beautifully crafted<br>luxury homes you'll<br>fall in love with.</h3>
  </div>
  <div class="btn btn-outline-white" style="left:744px;top:286px;width:158px;height:39px;font-size:14px">Read more</div>
</section>

<section class="contact">
  <h2>Get in touch</h2>
  <div class="field" style="left:234px;top:234px;width:331px;height:41px">Your Name</div>
  <div class="field" style="left:602px;top:234px;width:329px;height:41px">Your Phone</div>
  <div class="field" style="left:234px;top:304px;width:331px;height:41px">Email Address</div>
  <div class="field" style="left:602px;top:304px;width:329px;height:41px">Select Service</div>
  <div class="field" style="left:234px;top:370px;width:697px;height:88px">Additional Message</div>
  <div class="submit">Get an appointment now</div>
</section>

<footer class="footer">
  <div class="footer-brand">Tarvond<br>Constructions</div>
  <h4 style="left:329px">Contact us</h4>
  <h4 style="left:662px">Quick Links</h4>
  <h4 style="left:933px">Connect with us</h4>
  <div class="line" style="left:333px;top:180px">
    <svg width="16" height="16" viewBox="0 0 24 24"><path fill="#8dc63f" d="M6.6 10.8a15 15 0 0 0 6.6 6.6l2.2-2.2c.3-.3.7-.4 1-.2 1.1.4 2.3.6 3.6.6.6 0 1 .4 1 1V20c0 .6-.4 1-1 1A17 17 0 0 1 3 4c0-.6.4-1 1-1h3.5c.6 0 1 .4 1 1 0 1.3.2 2.5.6 3.6.1.3 0 .7-.2 1z"/></svg>
    (+61) 555 014 278
  </div>
  <div class="line" style="left:333px;top:227px">
    <svg width="16" height="13" viewBox="0 0 24 18"><rect x="1" y="1" width="22" height="16" rx="2" fill="#8dc63f"/><path d="M2 2l10 8 10-8" stroke="#3a3d47" stroke-width="2" fill="none"/></svg>
    support@domain.com
  </div>
  <div class="line" style="left:333px;top:275px">
    <svg width="14" height="18" viewBox="0 0 24 32"><path fill="#8dc63f" d="M12 0a12 12 0 0 0-12 12c0 9 12 20 12 20s12-11 12-20A12 12 0 0 0 12 0zm0 17a5 5 0 1 1 0-10 5 5 0 0 1 0 10z"/></svg>
    14 Harbour Lane, Kelmscott
  </div>
  <div class="link" style="left:663px;top:183px">Home</div>
  <div class="link" style="left:663px;top:215px">About</div>
  <div class="link" style="left:663px;top:247px">Services</div>
  <div class="link" style="left:663px;top:279px">Contact</div>
  <div class="social"><span></span><span></span><span></span></div>
</footer>

</div>
</body>
</html>
```